Storm Restoration Contractor needs a professional business card design

Looking for a professional business card design. Not looking for your cheapo MS Word standard ones that are readily available. Dont want it to be cookie cutter look like ones readily available online. We just recently changed our logo and want to freshen up all our documents. Our company handles restoring a property back to a pre-loss condition after a storm damages it. For example, wind, hail, flood, fire losses.

Target Market(s)

Property Owners, Homeowners, Property Owners, Commercial Property Owners, Property Management Companies, Hail and Wind Damaged Properties

Industry/Entity Type

Construction Company

Contact Information for Business Card

Halden Facades
847-519-4073
847-519-6294 fax
www.haldenfacades.example
info@haldenfacades.example

Requirements
Must have
• Clean, Professional, fresh look
• Storm Restoration, Roofing, Siding, Windows
Nice to have
• If there is a way to incorporate storms that may be cool.

```html
<!DOCTYPE html>
<html lang="en">
<head>
<meta charset="utf-8">
<title>Halden Facades – Business Card</title>
<link href="https://fonts.googleapis.com/css2?family=Roboto:wght@300;400;700&display=swap" rel="stylesheet">
<style>
  :root {
    --bg: #e9eaec;
    --card-white: #ffffff;
    --brand-blue: #1c7cc4;
    --brand-blue-dark: #0f66ab;
    --divider-grey: #58595b;
    --card-dark: #4a4b4d;
    --text-light: #ffffff;
    --text-soft: #d8e8f5;
    --text-muted: #c9cacc;
  }
  * { margin: 0; padding: 0; box-sizing: border-box; }
  html, body { width: 1200px; height: 950px; overflow: hidden; }
  body {
    background: var(--bg);
    font-family: "Roboto", Arial, sans-serif;
    position: relative;
  }
  .card {
    position: absolute;
    left: 250px;
    width: 700px;
    height: 400px;
    border-radius: 22px;
    overflow: hidden;
    box-shadow: 0 10px 30px rgba(0,0,0,0.18);
  }
  .card--front { top: 45px; background: var(--card-white); }
  .card--back { top: 505px; background: var(--card-dark); }

  .front-shape { position: absolute; inset: 0; width: 100%; height: 100%; }

  .brand {
    position: absolute;
    display: flex;
    align-items: center;
    gap: 14px;
  }
  .brand__circle {
    width: 58px; height: 58px;
    border-radius: 50%;
    flex: none;
  }
  .brand__name {
    font-weight: 700;
    font-size: 26px;
    letter-spacing: 1px;
    text-transform: uppercase;
    line-height: 1;
  }
  .card--front .brand { left: 48px; top: 150px; }
  .card--front .brand__circle { border: 5px solid var(--brand-blue); }
  .card--front .brand__name { color: var(--brand-blue); }

  .contact {
    position: absolute;
    right: 40px;
    bottom: 48px;
    width: 360px;
    text-align: right;
    color: var(--text-light);
  }
  .contact__name { font-size: 20px; font-weight: 700; }
  .contact__role { font-weight: 300; font-size: 16px; }
  .contact__rule {
    height: 1px;
    background: rgba(255,255,255,0.7);
    margin: 12px 0 12px 40px;
  }
  .contact__line { font-size: 13px; font-weight: 300; line-height: 1.7; }
  .contact__line b { font-weight: 700; }
  .contact__web {
    margin-top: 8px;
    font-size: 13px;
    font-weight: 300;
    letter-spacing: 3px;
    color: var(--text-soft);
  }

  .card--back .brand {
    left: 50%; top: 150px;
    transform: translateX(-50%);
  }
  .card--back .brand__circle { border: 5px solid var(--text-light); }
  .card--back .brand__name { color: var(--text-light); }
  .back-web {
    position: absolute;
    left: 0; right: 0; top: 248px;
    text-align: center;
    font-size: 13px;
    font-weight: 300;
    letter-spacing: 3px;
    color: var(--text-muted);
  }
</style>
</head>
<body>
  <section class="card card--front">
    <svg class="front-shape" viewBox="0 0 700 400" preserveAspectRatio="none" aria-hidden="true">
      <defs>
        <linearGradient id="blueFill" x1="0" y1="0" x2="1" y2="1">
          <stop offset="0" stop-color="var(--brand-blue)"/>
          <stop offset="1" stop-color="var(--brand-blue-dark)"/>
        </linearGradient>
      </defs>
      <path d="M470 0 C 420 150, 330 290, 150 400 L 700 400 L 700 0 Z" fill="var(--divider-grey)"/>
      <path d="M486 0 C 440 150, 352 292, 176 400 L 700 400 L 700 0 Z" fill="url(#blueFill)"/>
    </svg>
    <div class="brand">
      <span class="brand__circle"></span>
      <span class="brand__name">Halden Facades</span>
    </div>
    <div class="contact">
      <p class="contact__name">Marcus Vell <span class="contact__role">- President</span></p>
      <div class="contact__rule"></div>
      <p class="contact__line"><b>P:</b> 847-519-4073 &nbsp;<b>F:</b> 847-519-6294</p>
      <p class="contact__line"><b>E:</b> info@haldenfacades.example</p>
      <p class="contact__web">www.haldenfacades.example</p>
    </div>
  </section>

  <section class="card card--back">
    <div class="brand">
      <span class="brand__circle"></span>
      <span class="brand__name">Halden Facades</span>
    </div>
    <p class="back-web">www.haldenfacades.example</p>
  </section>
</body>
</html>
```